Harold T. Wexley, MD

I would like to set up a web page for my new psychiatric practice. It should summarize my credentials and approach to care plus a patient portal to complete forms before appointments.
I am uploading a powerpoint with my contact information along with the color palette and format I would like to use. The email on the slide has not been reserved and I will need to reserve the domain as part of this process.

```html
<!DOCTYPE html>
<html lang="en">
<head>
<meta charset="utf-8">
<title>Harold T. Wexley, MD, MBA — Psychiatric Practice</title>
<link href="https://fonts.googleapis.com/css2?family=Open+Sans:wght@400;600;700;800&display=swap" rel="stylesheet">
<style>
  :root {
    --pink: #d91a5f;
    --pink-dark: #b3124c;
    --pink-soft: #e8467f;
    --ink: #3a3a3a;
    --muted: #6b6b6b;
    --form-bg: rgba(40, 30, 40, 0.78);
    --field: #8a2a4c;
    --white: #ffffff;
    --footer-bar: #e6e6e6;
  }
  * { box-sizing: border-box; margin: 0; padding: 0; }
  html, body { width: 882px; height: 1200px; overflow: hidden; }
  body { font-family: "Open Sans", Arial, sans-serif; background: var(--white); color: var(--ink); position: relative; }

  .site-header { position: absolute; top: 0; left: 0; width: 882px; height: 78px; background: var(--white); }
  .brand { position: absolute; left: 26px; top: 22px; }
  .brand-name { color: var(--pink); font-weight: 800; font-size: 19px; letter-spacing: 0.3px; }
  .brand-tag { color: var(--muted); font-size: 10px; text-align: center; margin-top: 2px; }
  .main-nav { position: absolute; right: 40px; top: 0; display: flex; height: 48px; }
  .main-nav a { font-size: 9px; font-weight: 600; color: var(--ink); text-decoration: none; padding: 0 10px; display: flex; align-items: center; height: 48px; }
  .main-nav a.active { background: var(--pink); color: var(--white); padding: 0 16px; }

  .hero { position: absolute; top: 78px; left: 0; width: 882px; height: 402px;
    background: linear-gradient(100deg, #dfe8ee 0%, #c9d7e0 40%, #e9eef2 70%, #f4f6f8 100%); }

  .booking { position: absolute; left: 528px; top: 150px; width: 330px; height: 290px; }
  .booking-title { background: var(--pink); color: var(--white); font-weight: 700; font-size: 17px; letter-spacing: 0.5px; padding: 10px 16px; height: 42px; }
  .booking-body { background: var(--form-bg); padding: 12px 16px; height: 248px; }
  .field-row { display: flex; gap: 10px; margin-bottom: 8px; }
  .field { flex: 1; height: 20px; background: var(--field); color: #f2d0dd; font-size: 8px; padding: 5px 8px; position: relative; }
  .field.select::after { content: ""; position: absolute; right: 8px; top: 8px; border: 4px solid transparent; border-top-color: #f2d0dd; }
  .field.message { height: 70px; }
  .submit { display: block; margin: 10px auto 0; width: 110px; height: 22px; background: var(--pink); color: var(--white); font-size: 9px; font-weight: 700; text-align: center; line-height: 22px; }

  .doctor-portrait { position: absolute; left: 40px; top: 488px; width: 258px; height: 556px;
    background: linear-gradient(180deg, #f1f1f1 0%, #e4e4e4 55%, #d6d6d6 100%); z-index: 2; }

  .about { position: absolute; left: 320px; top: 500px; width: 530px; }
  .about h2 { font-size: 15px; font-weight: 700; color: var(--ink); margin-bottom: 8px; }
  .about-rule { width: 100%; height: 2px; background: var(--pink); margin-bottom: 14px; }
  .about p { font-size: 10.5px; line-height: 1.6; color: var(--muted); margin-bottom: 10px; }
  .learn-more { display: inline-block; margin-top: 6px; background: var(--pink); color: var(--white); font-size: 10px; font-weight: 700; padding: 7px 22px; }

  .conditions { position: absolute; left: 0; top: 808px; width: 882px; height: 238px; background: var(--pink); }
  .conditions h2 { position: absolute; left: 320px; width: 530px; top: 22px; text-align: center; color: var(--white); font-size: 16px; font-weight: 700; letter-spacing: 0.5px; }
  .condition-list { position: absolute; top: 60px; left: 320px; width: 530px; display: grid; grid-template-columns: 1fr 1fr; column-gap: 20px; list-style: none; }
  .condition-list li { display: flex; align-items: center; gap: 8px; height: 34px; border-bottom: 1px solid rgba(255,255,255,0.4); color: var(--white); font-size: 9.5px; font-weight: 600; }
  .condition-list svg { flex: 0 0 auto; }

  .site-footer { position: absolute; left: 0; top: 1046px; width: 882px; height: 120px; }
  .footer-brand { position: absolute; left: 26px; top: 38px; }
  .footer-brand .brand-name { font-size: 14px; color: var(--ink); }
  .contact { position: absolute; top: 28px; text-align: center; font-size: 10px; color: var(--ink); font-weight: 600; line-height: 1.5; }
  .contact svg { display: block; margin: 0 auto 6px; }
  .contact.address { left: 400px; width: 160px; }
  .contact.phone { left: 590px; width: 110px; }
  .contact.email { left: 720px; width: 150px; }
  .copyright { position: absolute; left: 0; bottom: 0; width: 882px; height: 34px; background: var(--footer-bar); color: var(--muted); font-size: 8px; text-align: center; line-height: 34px; letter-spacing: 0.4px; }
</style>
</head>
<body>

<header class="site-header">
  <div class="brand">
    <div class="brand-name">HAROLD T. WEXLEY, MD, MBA</div>
    <div class="brand-tag">Psychiatric Practice</div>
  </div>
  <nav class="main-nav">
    <a class="active" href="#">HOME</a>
    <a href="#">ABOUT HAROLD T. WEXLEY, MD, MBA</a>
    <a href="#">CONDITIONS TREATED</a>
  </nav>
</header>

<section class="hero" role="img" aria-label="Photo of a smiling doctor holding a tablet in a bright clinic corridor"></section>

<form class="booking">
  <div class="booking-title">BOOK AN APPOINTMENT</div>
  <div class="booking-body">
    <div class="field-row"><div class="field">Name</div><div class="field">Phone Number</div></div>
    <div class="field-row"><div class="field">Email Address</div><div class="field select">Treatment</div></div>
    <div class="field-row"><div class="field select">Desired Date</div><div class="field select">Desired Hour</div></div>
    <div class="field-row"><div class="field message">Message/Comment</div></div>
    <div class="submit">SUBMIT</div>
  </div>
</form>

<div class="doctor-portrait" role="img" aria-label="Portrait photo of a doctor in a white coat standing with arms at his sides"></div>

<section class="about">
  <h2>ABOUT HAROLD T. WEXLEY, MD, MBA</h2>
  <div class="about-rule"></div>
  <p>Dr. Wexley is a board certified psychiatrist who offers thoughtful, evidence based care for adults facing mood, anxiety and memory concerns. Each visit begins with careful listening and a full review of history, so that treatment plans reflect the whole person. His practice combines medication management with supportive therapy and close coordination with primary care teams.</p>
  <p>New patients may complete intake forms through the secure portal before their first appointment. This saves time in the office and lets each session focus on what matters most: your goals, your questions and a clear path toward feeling better.</p>
  <a class="learn-more">LEARN MORE</a>
</section>

<section class="conditions">
  <h2>CONDITIONS TREATED</h2>
  <ul class="condition-list">
    <li><svg width="12" height="12" viewBox="0 0 12 12"><circle cx="6" cy="6" r="6" fill="#fff"/><path d="M3.3 6.2 5.2 8 8.8 4" stroke="#d91a5f" stroke-width="1.6" fill="none"/></svg>Acute Stress Disorder and Post Traumatic Stress Disorder</li>
    <li><svg width="12" height="12" viewBox="0 0 12 12"><circle cx="6" cy="6" r="6" fill="#fff"/><path d="M3.3 6.2 5.2 8 8.8 4" stroke="#d91a5f" stroke-width="1.6" fill="none"/></svg>Major Depressive Disorder</li>
    <li><svg width="12" height="12" viewBox="0 0 12 12"><circle cx="6" cy="6" r="6" fill="#fff"/><path d="M3.3 6.2 5.2 8 8.8 4" stroke="#d91a5f" stroke-width="1.6" fill="none"/></svg>Alzheimer's Disease and Other Dementias</li>
    <li><svg width="12" height="12" viewBox="0 0 12 12"><circle cx="6" cy="6" r="6" fill="#fff"/><path d="M3.3 6.2 5.2 8 8.8 4" stroke="#d91a5f" stroke-width="1.6" fill="none"/></svg>Obsessive Compulsive Disorder</li>
    <li><svg width="12" height="12" viewBox="0 0 12 12"><circle cx="6" cy="6" r="6" fill="#fff"/><path d="M3.3 6.2 5.2 8 8.8 4" stroke="#d91a5f" stroke-width="1.6" fill="none"/></svg>Bipolar Disorder</li>
    <li><svg width="12" height="12" viewBox="0 0 12 12"><circle cx="6" cy="6" r="6" fill="#fff"/><path d="M3.3 6.2 5.2 8 8.8 4" stroke="#d91a5f" stroke-width="1.6" fill="none"/></svg>Panic Disorder</li>
    <li><svg width="12" height="12" viewBox="0 0 12 12"><circle cx="6" cy="6" r="6" fill="#fff"/><path d="M3.3 6.2 5.2 8 8.8 4" stroke="#d91a5f" stroke-width="1.6" fill="none"/></svg>Borderline Personality Disorder</li>
    <li><svg width="12" height="12" viewBox="0 0 12 12"><circle cx="6" cy="6" r="6" fill="#fff"/><path d="M3.3 6.2 5.2 8 8.8 4" stroke="#d91a5f" stroke-width="1.6" fill="none"/></svg>Schizophrenia</li>
    <li><svg width="12" height="12" viewBox="0 0 12 12"><circle cx="6" cy="6" r="6" fill="#fff"/><path d="M3.3 6.2 5.2 8 8.8 4" stroke="#d91a5f" stroke-width="1.6" fill="none"/></svg>Delirium</li>
    <li><svg width="12" height="12" viewBox="0 0 12 12"><circle cx="6" cy="6" r="6" fill="#fff"/><path d="M3.3 6.2 5.2 8 8.8 4" stroke="#d91a5f" stroke-width="1.6" fill="none"/></svg>Substance Use Disorders</li>
  </ul>
</section>

<footer class="site-footer">
  <div class="footer-brand">
    <div class="brand-name">HAROLD T. WEXLEY, MD, MBA</div>
    <div class="brand-tag">Psychiatric Practice</div>
  </div>
  <div class="contact address">
    <svg width="22" height="22" viewBox="0 0 22 22"><circle cx="11" cy="11" r="11" fill="#d91a5f"/><path d="M11 5a3.6 3.6 0 0 0-3.6 3.6c0 2.7 3.6 7.4 3.6 7.4s3.6-4.7 3.6-7.4A3.6 3.6 0 0 0 11 5z" fill="#fff"/><circle cx="11" cy="8.6" r="1.3" fill="#d91a5f"/></svg>
    PO Box 4120 PMB 305<br>Cedar Ridge, CA 90412
  </div>
  <div class="contact phone">
    <svg width="22" height="22" viewBox="0 0 22 22"><circle cx="11" cy="11" r="11" fill="#d91a5f"/><path d="M7.5 6h2l1 2.5-1.3 1a6 6 0 0 0 2.8 2.8l1-1.3 2.5 1v2c0 .6-.5 1-1 1A8.5 8.5 0 0 1 6.5 7c0-.5.4-1 1-1z" fill="#fff"/></svg>
    555-214-0198
  </div>
  <div class="contact email">
    <svg width="22" height="22" viewBox="0 0 22 22"><circle cx="11" cy="11" r="11" fill="#d91a5f"/><rect x="6" y="7.5" width="10" height="7" fill="#fff"/><path d="M6 7.5l5 4 5-4" stroke="#d91a5f" stroke-width="1" fill="none"/></svg>
    harold@wexleymd.com
  </div>
  <div class="copyright">COPYRIGHT © 2014 HAROLD T. WEXLEY, MD, MBA – PSYCHIATRIC PRACTICE</div>
</footer>

</body>
</html>
```